Korvanta Business Card

Looking for business card ideas. Company name is Korvanta. Have a few basic ideas on attachment. Please submit anything with the logo and general information from attachment.

Industry/Entity Type

Business

```html
<!DOCTYPE html>
<html lang="en">
<head>
<meta charset="utf-8">
<title>Korvanta Business Card</title>
<link href="https://fonts.googleapis.com/css2?family=Open+Sans:wght@400;600&display=swap" rel="stylesheet">
<style>
  :root {
    --backdrop: #222224;
    --card-brown: #3b2e26;
    --band-lilac: #dedbe8;
    --accent-blue: #2a86c8;
    --text-white: #ffffff;
  }
  * { margin: 0; padding: 0; box-sizing: border-box; }
  html, body {
    width: 1200px;
    height: 800px;
    overflow: hidden;
    background: var(--backdrop);
    font-family: "Open Sans", Arial, sans-serif;
  }
  .canvas {
    width: 1200px;
    height: 800px;
    display: flex;
    align-items: center;
    justify-content: center;
  }
  .business-card {
    position: relative;
    width: 840px;
    height: 480px;
    background: var(--card-brown);
    overflow: hidden;
  }
  .contact-person {
    position: absolute;
    left: 560px;
    top: 48px;
  }
  .person-name {
    color: var(--accent-blue);
    font-size: 24px;
    font-weight: 600;
    line-height: 1.2;
  }
  .person-role {
    color: var(--text-white);
    font-size: 16px;
    line-height: 1.2;
  }
  .brand-name {
    position: absolute;
    left: 60px;
    top: 176px;
    color: var(--text-white);
    font-size: 76px;
    font-weight: 400;
    line-height: 1;
    letter-spacing: 1px;
  }
  .info-band {
    position: absolute;
    left: 0;
    top: 282px;
    width: 100%;
    height: 132px;
    background: var(--band-lilac);
  }
  .info-group {
    position: absolute;
    color: var(--accent-blue);
    font-size: 17px;
    line-height: 1.75;
  }
  .phones { left: 300px; top: 12px; }
  .phones .label { display: inline-block; margin-left: 14px; }
  .address { left: 600px; top: 12px; }
  .online { left: 60px; top: 62px; }
</style>
</head>
<body>
  <main class="canvas">
    <article class="business-card">
      <div class="contact-person">
        <p class="person-name">Marlow Teague</p>
        <p class="person-role">Director</p>
      </div>

      <h1 class="brand-name">Korvanta</h1>

      <section class="info-band">
        <div class="info-group phones">
          <p>(555) 014-2281<span class="label">Cell</span></p>
          <p>(555) 014-7111<span class="label">Office</span></p>
        </div>
        <div class="info-group address">
          <p>Brenham, TX 70412</p>
          <p>418 S. Larkspur Ave</p>
        </div>
        <div class="info-group online">
          <p>www.korvanta.org</p>
          <p>mteague@korvanta.org</p>
        </div>
      </section>
    </article>
  </main>
</body>
</html>
```